IT COMPANYcutting edge tec business card

we are IT company that building any apps.
we need business card in japanese and english
You don’t have to include all information in front one you can attach part of that information to back-side
company name : 株式会社かすみ鳥 (MOSSLARK Inc.)
concept : cutting-edge technology
role : 取締役 (director)
name : 河 泰林 (Ha Taerimmu)
post number : 168-0037
address : 東京都世田谷区北霞台5-08-44 (5-08-44, Kitakasumidai, Setagaya Ku, Tokyo To, 168-0037, Japan)
Tel:+81-3-5917-2843
Mobile:+81-80-7263-5518
Email : taerimha@fieldoflark.com
website : www.fieldoflark.com

we dont have logo so please make it as well
we also looking for designer who can make homapage design.

Designs look the same

Low design quality

Contact Information for Business Card

cutting-edge design and modern for IT

Font styles to use
Sans Serif

Colors
34a6d7
33b8a4
6092c4
3377b5
886aae
6b449b
b868aa
a64599

Requirements
Must have
• Simple but designed

```html
<!DOCTYPE html>
<html lang="ja">
<head>
<meta charset="utf-8">
<title>MOSSLARK Inc. — Business Card</title>
<link href="https://fonts.googleapis.com/css2?family=Cinzel:wght@400&family=Open+Sans:wght@400;700&family=Noto+Sans+JP:wght@400;700&display=swap" rel="stylesheet">
<style>
  :root {
    --brand-blue: #34a6d7;
    --paper: #ffffff;
    --ink: #4a4a4a;
    --rule: #d6d6d6;
    --stage: #3b3b3b;
  }
  * { box-sizing: border-box; margin: 0; padding: 0; }
  html, body { width: 1200px; height: 1015px; overflow: hidden; }
  body {
    background: var(--stage);
    position: relative;
    font-family: "Open Sans", "Noto Sans JP", sans-serif;
  }
  .card {
    position: absolute;
    left: 230px;
    width: 740px;
    height: 448px;
    overflow: hidden;
    background: var(--paper);
  }

  /* Front */
  .card--front { top: 40px; }
  .front__name-field {
    position: absolute; left: 0; top: 0; width: 100%; height: 50%;
    background: var(--brand-blue);
    display: flex; align-items: center; justify-content: center;
  }
  .front__name {
    font-family: "Cinzel", serif;
    color: var(--paper);
    font-size: 58px;
    letter-spacing: 2px;
    padding-top: 30px;
  }
  .front__url-band {
    position: absolute; left: 0; top: 58%; width: 100%; height: 20%;
    background: var(--brand-blue);
    display: flex; align-items: center; justify-content: center;
  }
  .front__url {
    font-family: "Cinzel", serif;
    color: var(--paper);
    font-size: 20px;
    letter-spacing: 1.5px;
  }
  .front__edge {
    position: absolute; left: 0; bottom: 0; width: 100%; height: 8%;
    background: var(--brand-blue);
  }

  /* Back */
  .card--back { top: 527px; }
  .back__brand {
    position: absolute; left: 48px; top: 82px; width: 300px;
    display: flex; flex-direction: column; align-items: center; gap: 22px;
  }
  .back__brand-dot {
    width: 70px; height: 70px; border-radius: 50%;
    background: var(--brand-blue);
  }
  .back__brand-name {
    font-family: "Cinzel", serif;
    color: var(--brand-blue);
    font-size: 46px;
    letter-spacing: 1px;
  }
  .back__divider {
    position: absolute; left: 370px; top: 48px; width: 1px; height: 260px;
    background: var(--rule);
  }
  .contact {
    position: absolute; left: 392px; top: 52px; width: 330px;
    color: var(--ink); font-size: 14px; line-height: 1.45;
  }
  .contact__person { color: var(--brand-blue); font-weight: 700; font-size: 15px; }
  .contact__person .kanji { font-family: "Noto Sans JP", sans-serif; margin-right: 18px; }
  .contact__role .kanji { font-family: "Noto Sans JP", sans-serif; margin-right: 10px; }
  .contact__lines { list-style: none; margin-top: 4px; }
  .contact__lines li { display: flex; align-items: center; gap: 8px; }
  .contact__lines svg { width: 13px; height: 13px; flex: none; }
  .contact__company {
    margin-top: 10px; color: var(--brand-blue); font-weight: 700; font-size: 15px;
  }
  .contact__company .kanji { font-family: "Noto Sans JP", sans-serif; margin-right: 12px; }
  .contact__address .kanji { font-family: "Noto Sans JP", sans-serif; }
  .back__band {
    position: absolute; left: 0; bottom: 0; width: 100%; height: 27%;
    background: var(--brand-blue);
  }
  .back__url {
    position: absolute; right: 60px; top: 14px;
    color: var(--paper); font-size: 20px; letter-spacing: 0.5px;
  }
</style>
</head>
<body>

<section class="card card--front" aria-label="Card front">
  <div class="front__name-field"><span class="front__name">MOSSLARK</span></div>
  <div class="front__url-band"><span class="front__url">WWW.FIELDOFLARK.COM</span></div>
  <div class="front__edge"></div>
</section>

<section class="card card--back" aria-label="Card back">
  <div class="back__brand">
    <span class="back__brand-dot"></span>
    <span class="back__brand-name">MOSSLARK</span>
  </div>
  <div class="back__divider"></div>

  <div class="contact">
    <p class="contact__person"><span class="kanji">河 泰林</span>HA TAERIMMU</p>
    <p class="contact__role"><span class="kanji">取締役</span>Director</p>
    <ul class="contact__lines">
      <li>
        <svg viewBox="0 0 16 16" aria-hidden="true"><path fill="#4a4a4a" d="M1 5c0-2 3-3 7-3s7 1 7 3v1h-4V4.5H5V6H1zM3 7h10l1 7H2z"/></svg>
        +81-3-5917-2843
      </li>
      <li>
        <svg viewBox="0 0 16 16" aria-hidden="true"><rect x="2" y="2" width="12" height="12" fill="none" stroke="#4a4a4a" stroke-width="2"/></svg>
        +81-80-7263-5518
      </li>
      <li>
        <svg viewBox="0 0 16 16" aria-hidden="true"><rect x="1" y="3" width="14" height="10" fill="#4a4a4a"/><path d="M1 3l7 6 7-6" fill="none" stroke="#fff" stroke-width="1.5"/></svg>
        taerimha@fieldoflark.com
      </li>
    </ul>
    <p class="contact__company"><span class="kanji">株式会社かすみ鳥</span>MOSSLARK</p>
    <p class="contact__address">
      <span class="kanji">東京都世田谷区北霞台5-08-44</span><br>
      (5-08-44, Kitakasumidai,<br>
      Setagaya Ku,<br>
      Tokyo To, 168-0037, Japan)
    </p>
  </div>

  <div class="back__band"><span class="back__url">www.fieldoflark.com</span></div>
</section>

</body>
</html>
```